Business Card Design for Pastor/Church Leadership - simple, elegant, "different"

Design a name card based on logo and color from our branding guide - see file "MBF Logo and Color".
The teal frame around the logo is not part of the logo and is a not necessary design element for the name card (as the attached PDF file may suggest).
The font suggested by branding is "Frutiger 55 Roman".
The file "not good.pdf", a sample of a name card that is NOT good.
- fonts too small to read
- the tagline on the logo "Still waters, open door" not easy to read with logo used in this design
- "MAPLE GROVE FELLOWSHIP" unnecessarily duplicated - possibly because logo too small
- not sure about the green frame, probably better to drop

Target Market(s)

broad, all people the pastor of an international church in Tokyo meets

Industry/Entity Type

Business

Contact Information for Business Card

Mattias R. Pellworth
Pastor
3-9-4 Kawaranodai, Shibuya-ku
Tokyo 150-0001 (Church)
2-21 Ochibamachi, Shibuya-ku
Tokyo 150-0035 (Home)
Tel: 03-5817-2963
E-mail: pastor@maplegrovefell.org
URL: http://www.maplegrovefell.org

Font styles to use
Sans Serif
Other font styles liked:
• Frutiger 55 Roman (want, not must)

Requirements
Must have
• must include logo
• must make use of the "bright turquoise color"
• Cyan = 59, Magenta = 0, Yellow=24, Black=0
• Red=3.1%, Green=91%, Blue=87.1%
• Key Info (name) must be easy to read (see notes on bad sample namecard attached)

```html
<!DOCTYPE html>
<html lang="en">
<head>
<meta charset="utf-8">
<title>Maple Grove Fellowship – Pastor Business Card</title>
<link rel="stylesheet" href="https://fonts.googleapis.com/css2?family=Noto+Sans:wght@400;500&display=swap">
<style>
  :root {
    --teal: #5bc8ca;
    --teal-deep: #38aaa8;
    --paper: #ffffff;
    --backdrop: #e9eeee;
    --shadow: rgba(0, 0, 0, 0.18);
  }
  * { margin: 0; padding: 0; box-sizing: border-box; }
  html, body {
    width: 1200px; height: 1000px; overflow: hidden;
    background: var(--backdrop);
    font-family: "Noto Sans", "Frutiger", Arial, sans-serif;
  }
  .stage { position: relative; width: 1200px; height: 1000px; }

  .card {
    position: absolute;
    width: 540px; height: 310px;
    background: var(--paper);
    box-shadow: 0 6px 18px var(--shadow);
    overflow: hidden;
  }
  .card--front { left: 80px; top: 140px; }
  .card--back { left: 580px; top: 520px; }

  .front-art { position: absolute; inset: 0; }

  .identity {
    position: absolute; left: 36px; top: 50px;
    color: var(--paper);
  }
  .identity__name { font-size: 22px; font-weight: 400; line-height: 1.15; }
  .identity__role { font-size: 22px; font-weight: 400; line-height: 1.15; }
  .identity__rule { width: 112px; height: 2px; background: var(--paper); margin-top: 10px; }

  .contact {
    position: absolute; left: 36px; top: 142px;
    list-style: none; color: var(--paper); font-size: 13px;
  }
  .contact li { display: flex; align-items: center; gap: 9px; height: 24px; }
  .contact svg { width: 16px; height: 16px; flex: none; }

  .brand {
    position: absolute; left: 358px; top: 26px; width: 164px;
    color: var(--teal);
  }
  .brand__mark {
    font-size: 46px; font-weight: 500; letter-spacing: 2px;
    line-height: 1; padding-left: 22px;
  }
  .brand__name {
    margin-top: 24px; font-size: 11px; font-weight: 500; letter-spacing: 0.8px;
    white-space: nowrap;
  }
  .brand__rule { height: 1.5px; background: var(--teal); margin: 5px 0; width: 164px; }
  .brand__tagline { font-size: 12.5px; white-space: nowrap; }

  .address {
    position: absolute; color: var(--teal); font-size: 12.5px; line-height: 1.5;
    white-space: nowrap;
  }
  .address--church { left: 350px; top: 190px; }
  .address--home { left: 34px; top: 248px; }

  .back-brand {
    position: absolute; inset: 0;
    display: flex; flex-direction: column; align-items: center; justify-content: center;
    color: var(--teal);
  }
  .back-brand__mark { font-size: 96px; font-weight: 500; letter-spacing: 4px; line-height: 1; margin-top: -10px; }
  .back-brand__tagline { font-size: 19px; letter-spacing: 1.2px; margin-top: 44px; }
</style>
</head>
<body>
<main class="stage">

  <section class="card card--front" aria-label="Business card front">
    <svg class="front-art" viewBox="0 0 540 310" aria-hidden="true">
      <path d="M0 0 H296 C300 100 318 180 362 240 H0 Z" fill="var(--teal-deep)"/>
      <path d="M0 0 H282 C286 100 302 180 344 240 H0 Z" fill="var(--teal)"/>
      <rect x="0" y="292" width="540" height="18" fill="var(--teal-deep)"/>
    </svg>

    <div class="identity">
      <p class="identity__name">Mattias R. Pellworth</p>
      <p class="identity__role">Pastor</p>
      <div class="identity__rule"></div>
    </div>

    <ul class="contact">
      <li>
        <svg viewBox="0 0 16 16" aria-hidden="true"><path fill="currentColor" d="M2 5c0-2 2-3 6-3s6 1 6 3v1h-3V5H5v1H2zM4 7h8l2 6H2zm4 1.5a2 2 0 1 0 0 4 2 2 0 0 0 0-4z"/></svg>
        03-5817-2963
      </li>
      <li>
        <svg viewBox="0 0 16 16" aria-hidden="true"><rect x="1" y="3.5" width="14" height="9.5" fill="currentColor"/><path d="M1.5 4l6.5 5 6.5-5" stroke="var(--teal)" stroke-width="1.3" fill="none"/></svg>
        pastor@maplegrovefell.org
      </li>
      <li>
        <svg viewBox="0 0 16 16" aria-hidden="true" fill="none" stroke="currentColor" stroke-width="1.3"><circle cx="8" cy="8" r="6.5"/><ellipse cx="8" cy="8" rx="3" ry="6.5"/><path d="M1.5 8h13M2.5 4.8h11M2.5 11.2h11"/></svg>
        www.maplegrovefell.org
      </li>
    </ul>

    <div class="brand">
      <p class="brand__mark">MBF</p>
      <p class="brand__name">MAPLE GROVE FELLOWSHIP</p>
      <div class="brand__rule"></div>
      <p class="brand__tagline">Still waters, open door</p>
    </div>

    <p class="address address--church">3-9-4 Kawaranodai, Shibuya-ku<br>Tokyo 150-0001 (CHURCH)</p>
    <p class="address address--home">2-21 Ochibamachi, Shibuya-ku<br>Tokyo 150-0035 (HOME)</p>
  </section>

  <section class="card card--back" aria-label="Business card back">
    <div class="back-brand">
      <p class="back-brand__mark">MBF</p>
      <p class="back-brand__tagline">Still waters, open door</p>
    </div>
  </section>

</main>
</body>
</html>
```